Business cards and logo for a international shipping company called Meridane Freight LLC. We would like to incorporate the colors red and blue. We would like the theme to be nautical.

Industry/Entity Type

Business

```html
<!DOCTYPE html>
<html lang="en">
<head>
<meta charset="utf-8">
<title>Meridane Freight LLC — Business Card</title>
<link rel="stylesheet" href="https://fonts.googleapis.com/css2?family=Roboto:wght@300;500&family=Ubuntu:wght@500&display=swap">
<style>
  :root {
    --backdrop: #776d6a;
    --navy-slate: #4a6479;
    --sky: #40bdee;
    --signal-red: #d63b3b;
    --paper: #f5f5f5;
    --ink: #2f5270;
    --teal: #3aaebf;
    --watermark: #e3e8ec;
  }
  * { margin: 0; padding: 0; box-sizing: border-box; }
  html, body {
    width: 1200px; height: 1200px; overflow: hidden;
    background: var(--backdrop);
  }
  .card {
    position: absolute; left: 278px; width: 674px;
    overflow: hidden; background: var(--paper);
  }
  .card--front { top: 109px; height: 414px; }
  .card--back  { top: 618px; height: 418px; }

  .stripes { position: absolute; top: 0; height: 100%; }
  .stripe { position: absolute; left: 0; width: 100%; }
  .stripe--dark { background: var(--navy-slate); }
  .stripe--light { background: var(--sky); }
  .stripe--pin { background: var(--signal-red); height: 4px; }

  .card--front .stripes--left  { left: 0; width: 184px; }
  .card--front .stripes--right { left: 491px; width: 183px; }
  .card--back .stripes--left   { left: 0; width: 277px; }

  .brand-mark {
    position: absolute; left: 286px; top: 133px;
    width: 100px; height: 100px; border-radius: 50%;
    background: var(--signal-red);
  }
  .brand-name {
    position: absolute; left: 184px; width: 307px; top: 290px;
    text-align: center;
    font-family: "Ubuntu", sans-serif; font-weight: 500;
    font-size: 23px; color: var(--ink); letter-spacing: 0.2px;
  }
  .brand-wave {
    position: absolute; left: 297px; top: 334px;
    width: 80px; height: 12px;
  }

  .holder-name {
    position: absolute; left: 322px; top: 102px;
    font-family: "Roboto", sans-serif; font-weight: 300;
    font-size: 34px; color: var(--ink); letter-spacing: 0.5px;
  }
  .holder-rule {
    position: absolute; left: 322px; top: 155px;
    width: 48px; height: 2px; background: var(--signal-red);
  }
  .contact-list { list-style: none; }
  .contact {
    position: absolute; left: 320px; height: 34px;
    display: flex; align-items: center;
    font-family: "Roboto", sans-serif; font-weight: 500;
    font-size: 18.5px; color: var(--teal);
  }
  .contact svg { width: 34px; height: 34px; margin-right: 16px; flex: none; }
  .contact--phone { top: 175px; }
  .contact--email { top: 226px; }
  .contact--web   { top: 278px; }

  .corner-seal {
    position: absolute; left: 570px; top: 340px;
    width: 150px; height: 150px; border-radius: 50%;
    background: var(--watermark);
  }
</style>
</head>
<body>
  <section class="card card--front">
    <div class="stripes stripes--left">
      <div class="stripe stripe--dark" style="top:0;height:102px"></div>
      <div class="stripe stripe--light" style="top:102px;height:70px"></div>
      <div class="stripe stripe--pin" style="top:170px"></div>
      <div class="stripe stripe--dark" style="top:174px;height:69px"></div>
      <div class="stripe stripe--light" style="top:243px;height:70px"></div>
      <div class="stripe stripe--pin" style="top:311px"></div>
      <div class="stripe stripe--dark" style="top:315px;height:99px"></div>
    </div>
    <div class="stripes stripes--right">
      <div class="stripe stripe--dark" style="top:0;height:102px"></div>
      <div class="stripe stripe--light" style="top:102px;height:70px"></div>
      <div class="stripe stripe--pin" style="top:170px"></div>
      <div class="stripe stripe--dark" style="top:174px;height:69px"></div>
      <div class="stripe stripe--light" style="top:243px;height:70px"></div>
      <div class="stripe stripe--pin" style="top:311px"></div>
      <div class="stripe stripe--dark" style="top:315px;height:99px"></div>
    </div>
    <div class="brand-mark"></div>
    <h1 class="brand-name">Meridane Freight LLC</h1>
    <svg class="brand-wave" viewBox="0 0 80 12" aria-hidden="true"><path d="M2 6q9.5-7 19 0t19 0 19 0 19 0" fill="none" stroke="#d63b3b" stroke-width="2" stroke-linecap="round"/></svg>
  </section>

  <section class="card card--back">
    <div class="stripes stripes--left">
      <div class="stripe stripe--dark" style="top:0;height:103px"></div>
      <div class="stripe stripe--light" style="top:103px;height:70px"></div>
      <div class="stripe stripe--pin" style="top:171px"></div>
      <div class="stripe stripe--dark" style="top:175px;height:69px"></div>
      <div class="stripe stripe--light" style="top:244px;height:71px"></div>
      <div class="stripe stripe--pin" style="top:313px"></div>
      <div class="stripe stripe--dark" style="top:317px;height:101px"></div>
    </div>
    <div class="corner-seal"></div>
    <h2 class="holder-name">YOUR NAME</h2>
    <div class="holder-rule"></div>
    <ul class="contact-list">
      <li class="contact contact--phone">
        <svg viewBox="0 0 24 24" aria-hidden="true"><path fill="#2f5270" d="M6.6 3.2c.5-.4 1.2-.3 1.6.2l2.2 3c.3.5.3 1.1-.1 1.5L9 9.2c.8 2 2.9 4.2 5 5.1l1.3-1.3c.4-.4 1-.5 1.5-.1l3 2.1c.5.4.6 1.1.2 1.6l-1.5 2c-.6.8-1.7 1.1-2.7.8C10.6 18 6 13.4 4.4 8.2c-.3-1 0-2 .8-2.6z"/></svg>
        000-000-000
      </li>
      <li class="contact contact--email">
        <svg viewBox="0 0 24 24" aria-hidden="true"><rect x="2.5" y="5.5" width="19" height="13" fill="none" stroke="#2f5270" stroke-width="1.6"/><path d="M2.5 5.5l9.5 7.5 9.5-7.5M2.5 18.5l7-6M21.5 18.5l-7-6" fill="none" stroke="#2f5270" stroke-width="1.6"/></svg>
        hello@meridanefreight.net
      </li>
      <li class="contact contact--web">
        <svg viewBox="0 0 24 24" aria-hidden="true"><g fill="none" stroke="#2f5270" stroke-width="1.6"><circle cx="12" cy="12" r="9.5"/><ellipse cx="12" cy="12" rx="4.2" ry="9.5"/><path d="M12 2.5v19M2.5 12h19M4 7.5h16M4 16.5h16"/></g></svg>
        www.meridanefreight.net
      </li>
    </ul>
  </section>
</body>
</html>
```